Velmora ICT is an ICT Project Services, ICT Architecture and Cloud consultation service business. I need a web site that is simple and looks professional and can grow with my business. I'll leave the creativity and colours up to you as the creative professionals.
Our ICT Project Services specialise in small to medium ICT Projects for government agencies and private organisations and Defence. Our project consultancy services helps our clients get to project execution, Projects as a Service. More information on the offering to be provided.
Cloud services consultation aide and manage in getting clients into the cloud, utilising our technical experience and project management.
I need additional tabs on the site to cater for my additional services.
I am about to offer Quintaris Cloud Certification which will be a paid monthly subscription.
I also require a tab that focuses on our developed Project software. Project as a service. Essentially a step by step application that controls and runs the project from execution to closure for small (complex service requests) projects under $100000.
Happy to provide much more information.
Small to medium business, government agencies
It Company
Velmora ICT
Business Project Management and Architectural Services
Project Management as a Service.
Velmora ICT Consultative Business, Project Management and Architectural Services
2 page
- Additional tabs for the additional products ICT Training and Project Management Applicaiton

```html
<!DOCTYPE html>
<html lang="en">
<head>
<meta charset="utf-8">
<title>Velmora ICT</title>
<link href="https://fonts.googleapis.com/css2?family=Chakra+Petch:wght@400;500&family=Lato:wght@400;700;900&family=Open+Sans:wght@400;600;700&family=Raleway:wght@400&display=swap" rel="stylesheet">
<style>
  :root{
    --navy:#0b4a7e;
    --navy-deep:#09416f;
    --orange:#f7861f;
    --ink:#333a40;
    --slate:#4a5660;
    --muted:#8a8f94;
    --line:#dfe3e7;
    --white:#ffffff;
    --display:"Chakra Petch", sans-serif;
    --ui:"Lato", sans-serif;
    --body:"Open Sans", sans-serif;
    --banner:"Raleway", sans-serif;
  }
  *{box-sizing:border-box;margin:0;padding:0}
  html,body{width:687px;height:1200px;overflow:hidden;background:var(--white)}
  body{position:relative;font-family:var(--body);color:var(--ink)}
  a{color:inherit;text-decoration:none}

  /* header */
  .site-header{position:absolute;top:0;left:0;width:687px;height:54px}
  .brand{position:absolute;left:45px;top:4px;font-family:var(--display);font-weight:400;font-size:38px;color:var(--navy);letter-spacing:-0.5px;line-height:44px}
  .call{position:absolute;right:46px;top:10px;text-align:right;font-family:var(--ui)}
  .call-label{font-size:12px;color:var(--navy)}
  .call-number{margin-top:6px;font-size:12.5px;color:var(--orange);display:flex;align-items:center;gap:8px;justify-content:flex-end}

  .main-nav{position:absolute;top:54px;left:0;width:687px;height:26px;background:var(--navy)}
  .main-nav a{position:absolute;top:0;line-height:26px;font-family:var(--ui);font-size:10px;color:var(--white);transform:translateX(-50%)}

  /* hero */
  .hero{position:absolute;top:80px;left:0;width:687px;height:352px;
    background:linear-gradient(90deg,#e9c9d0 0%,#dfe6ee 22%,#e6ecf1 45%,#f3f3ef 100%)}
  .hero-photo{position:absolute;left:340px;top:0;width:240px;height:302px;
    background:linear-gradient(180deg,#c9cfd6 0%,#8f9cad 45%,#4a5d78 100%);border-radius:60px 60px 0 0}
  .hero-caption{position:absolute;left:26px;top:85px;width:332px;height:133px;background:rgba(190,210,228,.55);padding:14px 19px}
  .hero-caption h1{font-family:var(--ui);font-weight:900;font-size:25px;line-height:29px;color:#2f3438;letter-spacing:-0.5px}
  .hero-caption p{margin-top:8px;font-family:var(--ui);font-size:13px;line-height:20px;color:var(--navy)}

  .services{position:absolute;top:382px;left:80px;width:527px;height:113px;background:linear-gradient(180deg,#fff 70%,#eef5fb 100%);box-shadow:0 14px 30px rgba(0,0,0,.08);display:flex}
  .service{flex:1;position:relative;border-right:1px solid var(--line);padding:27px 0 0 52px}
  .service:last-child{border-right:none}
  .service-icon{position:absolute;left:10px;top:30px;width:36px;height:36px;border:1.5px solid #3a3f44;border-radius:50%;display:flex;align-items:center;justify-content:center}
  .service h3{font-family:var(--display);font-weight:400;font-size:13.5px;color:var(--orange)}
  .service p{margin-top:6px;font-size:7.5px;line-height:13px;color:var(--muted);width:120px}
  .service .more{margin-top:3px;display:block;font-family:var(--ui);font-size:11px;color:#2f3438}
  .service .more.active{color:var(--orange)}

  /* welcome */
  .welcome-title{position:absolute;top:518px;left:0;width:687px;text-align:center;font-family:var(--display);font-weight:400;font-size:30px;color:var(--slate)}
  .welcome-title span{color:var(--orange)}
  .welcome-copy{position:absolute;left:45px;top:566px;width:362px}
  .welcome-copy p{font-size:8.8px;line-height:14.3px;color:#4a4f54;margin-bottom:11px}
  .btn{position:absolute;left:45px;top:664px;width:89px;height:27px;background:#4d5a63;border-radius:2px;color:var(--white);font-family:var(--ui);font-size:11.5px;line-height:27px;text-align:center}
  .video{position:absolute;left:420px;top:565px;width:223px;height:113px;background:radial-gradient(ellipse at 50% 40%,#4a4d52 0%,#2a2c30 100%);display:flex;align-items:center;justify-content:center}
  .play{width:30px;height:22px;background:var(--white);border-radius:5px;display:flex;align-items:center;justify-content:center}

  /* certification band */
  .cert-band{position:absolute;top:722px;left:0;width:687px;height:89px;background:var(--navy-deep)}
  .cert-band p{position:absolute;left:62px;top:20px;font-family:var(--banner);font-size:17.5px;line-height:24px;color:var(--white)}
  .cert-badge{position:absolute;left:432px;top:18px;width:192px;height:56px;border:2px solid rgba(255,255,255,.85);border-radius:4px}

  /* sectors */
  .sectors-title{position:absolute;top:835px;left:0;width:687px;text-align:center;font-family:var(--display);font-weight:400;font-size:30px;color:var(--slate)}
  .sector{position:absolute;top:883px;width:168px}
  .sector-photo{width:168px;height:86px}
  .sector h3{margin-top:8px;font-family:var(--banner);font-size:14px;color:var(--slate);font-weight:400}
  .sector.featured h3{color:var(--orange)}
  .sector p{margin-top:5px;font-size:8px;line-height:13px;color:var(--muted)}
  .sector .more{display:inline-block;margin-top:6px;font-family:var(--ui);font-size:12px;color:var(--slate);text-decoration:underline}
  .sector.featured .more{color:var(--orange)}

  /* footer */
  .site-footer{position:absolute;top:1076px;left:0;width:687px;height:124px;background:var(--navy)}
  .footer-nav{position:absolute;left:45px;top:26px;display:flex;gap:0}
  .footer-nav a{font-family:var(--ui);font-size:9.5px;color:var(--white);margin-right:30px}
  .social{position:absolute;right:44px;top:17px;display:flex;gap:6px}
  .social span{width:24px;height:24px;border:1.5px solid var(--white)}
  .social span:first-child{background:var(--white)}
  .footer-rule{position:absolute;left:45px;right:44px;top:56px;height:1px;background:rgba(255,255,255,.3)}
  .contact-item{position:absolute;top:66px;display:flex;gap:7px;align-items:flex-start;color:var(--white);font-size:7.8px;line-height:13px}
  .contact-item strong{font-weight:700;display:block}
  .copyright{position:absolute;left:0;top:107px;width:687px;text-align:center;font-size:8px;color:var(--white);font-weight:600}
  .copyright span{color:#5fb0ec}
</style>
</head>
<body>

<header class="site-header">
  <div class="brand">Velmora ICT</div>
  <div class="call">
    <div class="call-label">Call Us Now</div>
    <div class="call-number">
      <svg width="12" height="12" viewBox="0 0 24 24"><path fill="#0b4a7e" d="M6.6 10.8a15.1 15.1 0 0 0 6.6 6.6l2.2-2.2c.3-.3.7-.4 1-.2 1.1.4 2.3.6 3.6.6.6 0 1 .4 1 1V20c0 .6-.4 1-1 1A17 17 0 0 1 3 4c0-.6.4-1 1-1h3.5c.6 0 1 .4 1 1 0 1.3.2 2.5.6 3.6.1.3 0 .7-.2 1z"/></svg>
      +(555) 014 2290
    </div>
  </div>
</header>

<nav class="main-nav">
  <a href="#" style="left:110px">HOME</a>
  <a href="#" style="left:198px">ABOUT</a>
  <a href="#" style="left:290px">SERVICES</a>
  <a href="#" style="left:388px">SECTORS</a>
  <a href="#" style="left:478px">NEWS</a>
  <a href="#" style="left:570px">CONTACT</a>
</nav>

<section class="hero">
  <div class="hero-photo" role="img" aria-label="Businessman holding a tablet, double exposure with city skyscrapers"></div>
  <div class="hero-caption">
    <h1>LOREM IPSUM IS SIMPLY DUMMY TEXT.</h1>
    <p>Lorem Ipsum is simply dummy text of the printing and typesetting industry.</p>
  </div>
</section>

<section class="services">
  <article class="service">
    <div class="service-icon"><svg width="16" height="16" viewBox="0 0 16 16"><rect x="2" y="2" width="10" height="12" fill="none" stroke="#333" stroke-width="1.4"/><path d="M4 5h6M4 8h6M4 11h3" stroke="#333" stroke-width="1.2"/></svg></div>
    <h3>ICT Project</h3>
    <p>Lorem Ipsum is simply dummy text of the printing...</p>
    <a class="more active" href="#">READ MORE »</a>
  </article>
  <article class="service">
    <div class="service-icon"><svg width="16" height="16" viewBox="0 0 16 16"><rect x="6" y="1" width="4" height="4" fill="#333"/><rect x="1" y="11" width="4" height="4" fill="#333"/><rect x="6" y="11" width="4" height="4" fill="#333"/><rect x="11" y="11" width="4" height="4" fill="#333"/><path d="M8 5v6M3 11V8h10v3" fill="none" stroke="#333" stroke-width="1.2"/></svg></div>
    <h3>ICT Architecture</h3>
    <p>Lorem Ipsum is simply dummy text of the printing...</p>
    <a class="more" href="#">READ MORE »</a>
  </article>
  <article class="service">
    <div class="service-icon"><svg width="16" height="16" viewBox="0 0 16 16"><circle cx="4" cy="4" r="2" fill="#333"/><circle cx="12" cy="4" r="2" fill="#333"/><rect x="5" y="8" width="6" height="4" fill="#333"/><path d="M2 8v6M14 8v6M8 12v3" stroke="#333" stroke-width="1.4"/></svg></div>
    <h3>Cloud consultation</h3>
    <p>Lorem Ipsum is simply dummy text of the printing...</p>
    <a class="more" href="#">READ MORE »</a>
  </article>
</section>

<h2 class="welcome-title">Welcome To <span>Velmora ICT</span></h2>
<div class="welcome-copy">
  <p>Lorem Ipsum is simply dummy text of the printing and typesetting industry. Lorem Ipsum has been the industry's standard dummy text ever since the 1500s, when an unknown printer took a galley of type and scrambled it to make a type specimen book.</p>
  <p>Lorem Ipsum is simply dummy text of the printing and typesetting industry. Lorem Ipsum has been the industry's standard dummy text ever since the 1500s.</p>
</div>
<a class="btn" href="#">READ MORE</a>
<div class="video" role="img" aria-label="Video: cloud connected to laptops, phones and monitors">
  <div class="play"><svg width="10" height="12" viewBox="0 0 10 12"><path d="M0 0l10 6-10 6z" fill="#222"/></svg></div>
</div>

<section class="cert-band">
  <p>We offer Quintaris Cloud Certification<br>which will be a paid monthly subscription.</p>
  <div class="cert-badge" role="img" aria-label="Quintaris certified badge"></div>
</section>

<h2 class="sectors-title">Sectors</h2>
<article class="sector featured" style="left:44px">
  <div class="sector-photo" role="img" aria-label="Government capitol building dome under blue sky" style="background:linear-gradient(180deg,#2f67b8 0%,#6a98d4 55%,#e6e3dc 100%)"></div>
  <h3>Government Agencies</h3>
  <p>Lorem Ipsum is simply dummy text of the printing and typesetting industry.</p>
  <a class="more" href="#">READ MORE</a>
</article>
<article class="sector" style="left:259px">
  <div class="sector-photo" role="img" aria-label="Business meeting around a conference table" style="background:linear-gradient(180deg,#b98a7c 0%,#7a5446 50%,#3c2c28 100%)"></div>
  <h3>Private Organisations</h3>
  <p>Lorem Ipsum is simply dummy text of the printing and typesetting industry.</p>
  <a class="more" href="#">READ MORE</a>
</article>
<article class="sector" style="left:475px">
  <div class="sector-photo" role="img" aria-label="Hands protecting a glowing cloud symbol" style="background:radial-gradient(ellipse at 55% 50%,#3d6f9e 0%,#17304f 60%,#0c1a2e 100%)"></div>
  <h3>Defence</h3>
  <p>Lorem Ipsum is simply dummy text of the printing and typesetting industry.</p>
  <a class="more" href="#">READ MORE</a>
</article>

<footer class="site-footer">
  <nav class="footer-nav">
    <a href="#">HOME</a><a href="#">ABOUT</a><a href="#">SERVICES</a><a href="#">SECTORS</a><a href="#">NEWS</a><a href="#">CONTACT</a>
  </nav>
  <div class="social" aria-label="Social links"><span></span><span></span><span></span><span></span></div>
  <div class="footer-rule"></div>
  <div class="contact-item" style="left:45px">
    <svg width="14" height="16" viewBox="0 0 14 16"><path d="M7 0v16M2 3h10l1.5 1.5L12 6H2zM1 8h9v3H1L0 9.5z" fill="#fff" stroke="#fff" stroke-width="1"/></svg>
    <div><strong>POSTAL ADDRESS</strong>123,Lorem Ipsum, City, Country - zipcode</div>
  </div>
  <div class="contact-item" style="left:259px;top:70px">
    <svg width="14" height="14" viewBox="0 0 24 24"><path fill="none" stroke="#fff" stroke-width="1.6" d="M6.6 10.8a15.1 15.1 0 0 0 6.6 6.6l2.2-2.2c.3-.3.7-.4 1-.2 1.1.4 2.3.6 3.6.6.6 0 1 .4 1 1V20c0 .6-.4 1-1 1A17 17 0 0 1 3 4c0-.6.4-1 1-1h3.5c.6 0 1 .4 1 1 0 1.3.2 2.5.6 3.6.1.3 0 .7-.2 1z"/></svg>
    <div>+(555) 014 2290</div>
  </div>
  <div class="contact-item" style="left:475px;top:70px">
    <svg width="15" height="12" viewBox="0 0 15 12"><rect x="0.8" y="0.8" width="13.4" height="10.4" rx="1" fill="none" stroke="#fff" stroke-width="1.3"/><path d="M1 1.5l6.5 5 6.5-5" fill="none" stroke="#fff" stroke-width="1.3"/></svg>
    <div>info@velmoraict.com</div>
  </div>
  <div class="copyright">© <span>Harlow Build Group</span> - 2016 All Right Reserved</div>
</footer>

</body>
</html>
```